I want to thank you very much for all your great designs. It was a really tough choice, but I have finally chosen a winner. I have been very happy with this process and very pleased with all the great choices I was given. I will definitely refer this company to my friends and tell them that they will get exactly what they are looking for from many, very talented designers. Thanks again! Dana
Hello All.
When doing that additional return address label,
Include:
- Logo
- Company Name
- Address
- Design Concept
- Size: 4"X3" (inches) return label
Thanks
Hello Designers! Great work that I'm seeing! If I have starred one of your designs, you should have received private messages regarding them by now. If not, please message me.
Can you please be sure to resubmit those designs with the changes I have requested because if I starred it, I'm considering it as my choice.
Don't forget to review the general comments in case I didn't add those things in your private messages.
One thing I wanted to add to the general comments is the fact that I somehow want "The Builder's Coverage Advisors" to be incorporated large on the back of the cards.
After I get the updated designs and I will re-star them. I would then like to start receiving the stationery layouts from the top designs I pick. Besides the letterhead and #10 return envelope I will also need a design for a return address label/sticker for a large 9X11 envelope.
Thanks for your participation. I look for to the updated designs. Dana
Hi. Thanks so much for all your designs. Just a couple of general comments.
I do like the more colorful cards using the gold as an accent only. I prefer the blue and black and white more for large sections or entire backgrounds.
I would like either spaces or periods between all the phone numbers, please. example: 555.418.3927 or 555 418 3927
License number can simply be License# .......
I haven't decided if I like the symbols next to the phone, fax, email, web yet. Can I see some different options instead of symbols so I can decide.
Thanks again for your time and great work. I look forward to choosing the winning design. Dana
I haven't decided if I like the symbols next to the phone, fax, email, web. Can I see some different options instead of symbols.
Thanks for your time and great work. I look forward to choosing the winning design. Dana
RT/PHW/NC Team
#8 I like this one too. Like the added info on back. Also can you please add the license number so I can see that on there. We have to advertise our insurance license for the company and individuals. Thanks
#2 I like this design. Please add & refer to the information requested on card in the design request area and the comments section for information on what info I want on the back. I'd like to see it with all my data, please. Please also add spacing or characters on the phone numbers. Thanks so much.

```html
<!DOCTYPE html>
<html lang="en">
<head>
<meta charset="utf-8">
<title>Halvorsen Insurance Services – Stationery</title>
<link rel="stylesheet" href="https://fonts.googleapis.com/css2?family=Montserrat:wght@700&family=Didact+Gothic&display=swap">
<style>
  :root{
    --navy:#1f3a5f;
    --gold:#c9a24a;
    --ink:#4a4f57;
    --muted:#8a9099;
    --rule:#cfd4da;
    --paper:#ffffff;
    --stage:#e9edf2;
  }
  *{box-sizing:border-box;margin:0;padding:0}
  html,body{width:1200px;height:1047px;overflow:hidden}
  body{background:var(--stage);font-family:"Didact Gothic",sans-serif;color:var(--ink);position:relative}
  .sheet{position:absolute;background:var(--paper);box-shadow:0 2px 10px rgba(20,40,70,.18)}
  .letterhead{left:140px;top:50px;width:440px;height:570px;padding:34px 36px}
  .fax-sheet{left:620px;top:50px;width:440px;height:570px;padding:34px 36px}
  .envelope{left:140px;top:690px;width:560px;height:243px;padding:24px 28px}
  .label{left:740px;top:690px;width:320px;height:243px;padding:24px 26px;border-radius:14px}

  .brand{display:flex;align-items:center;gap:8px}
  .brand-mark{width:16px;height:16px;background:var(--navy);flex:none}
  .brand-name{font-family:"Montserrat",sans-serif;font-weight:700;color:var(--navy);font-size:18px;line-height:1.05}
  .brand-name small{display:block;font-size:8px;letter-spacing:.12em}

  .contact{position:absolute;top:30px;right:30px;font-size:8px;line-height:1.55;color:var(--muted);text-align:left}
  .contact b{color:var(--gold);font-weight:normal;display:inline-block;width:10px}
  .contact .street{color:var(--ink)}

  .greeting{margin-top:70px;font-size:15px;color:var(--ink)}
  .body-copy{margin-top:14px;font-size:9.5px;line-height:1.75;color:var(--muted)}
  .body-copy p+p{margin-top:10px}
  .gold-rule{position:absolute;left:36px;right:36px;bottom:30px;height:2px;background:var(--gold)}

  .fax-title{margin-top:70px;font-size:26px;color:var(--navy)}
  .fax-form{margin-top:14px;border:1px solid var(--rule);border-radius:6px}
  .fax-row{display:flex;border-bottom:1px solid var(--rule);height:34px;align-items:center;padding:0 12px;font-size:10px;color:var(--muted)}
  .fax-row:last-child{border-bottom:none}
  .fax-row span{width:60px}
  .fax-notes{height:170px;padding:10px 12px;font-size:10px;color:var(--muted)}
  .recycle{margin-top:14px;display:flex;align-items:center;gap:6px;font-size:10px;color:var(--muted)}
  .recycle i{width:10px;height:10px;border:1px solid var(--muted);display:inline-block}

  .return-address{margin-top:12px;font-size:9px;line-height:1.5;color:var(--ink)}
  .envelope .gold-rule{left:28px;right:28px;bottom:18px}

  .label .brand-name{font-size:22px}
  .label .brand-mark{width:20px;height:20px}
  .label-address{margin-top:60px;text-align:center;font-size:16px;line-height:1.45;color:var(--ink)}
</style>
</head>
<body>

<section class="sheet letterhead">
  <div class="brand"><span class="brand-mark"></span><div class="brand-name">Halvorsen<small>INSURANCE SERVICES</small></div></div>
  <div class="contact">
    <div class="street">2290 Larkspur Lane #204</div>
    <div class="street">Alder Creek, CA 90817</div>
    <div><b>P</b>555 418 3927</div>
    <div><b>F</b>555 418 3928</div>
    <div><b>E</b>info@halvorseninsure.com</div>
    <div><b>W</b>www.halvorseninsure.com</div>
  </div>
  <div class="greeting">Hello,</div>
  <div class="body-copy">
    <p>Lorem ipsum dolor sit amet, consectetur adipiscing elit, sed do eiusmod tempor incididunt ut labore et dolore magna aliqua. Ut enim ad minim veniam, quis nostrud exercitation ullamco laboris nisi ut aliquip ex ea commodo consequat. Duis aute irure dolor in reprehenderit in voluptate velit esse cillum dolore eu fugiat nulla pariatur.</p>
    <p>Excepteur sint occaecat cupidatat non proident, sunt in culpa qui officia deserunt mollit anim id est laborum. Sed ut perspiciatis unde omnis iste natus error sit voluptatem accusantium doloremque laudantium, totam rem aperiam eaque ipsa quae ab illo.</p>
  </div>
  <div class="gold-rule"></div>
</section>

<section class="sheet fax-sheet">
  <div class="brand"><span class="brand-mark"></span><div class="brand-name">Halvorsen<small>INSURANCE SERVICES</small></div></div>
  <div class="contact">
    <div class="street">2290 Larkspur Lane #204</div>
    <div class="street">Alder Creek, CA 90817</div>
    <div><b>P</b>555 418 3927</div>
    <div><b>F</b>555 418 3928</div>
    <div><b>E</b>info@halvorseninsure.com</div>
    <div><b>W</b>www.halvorseninsure.com</div>
  </div>
  <div class="fax-title">Fax Sheet</div>
  <div class="fax-form">
    <div class="fax-row"><span>To:</span></div>
    <div class="fax-row"><span>From:</span></div>
    <div class="fax-row"><span>Date:</span></div>
    <div class="fax-row"><span>Pages:</span></div>
    <div class="fax-notes">Notes and comments:</div>
  </div>
  <div class="recycle"><i></i>Please Recycle</div>
  <div class="gold-rule"></div>
</section>

<section class="sheet envelope">
  <div class="brand"><span class="brand-mark"></span><div class="brand-name">Halvorsen<small>INSURANCE SERVICES</small></div></div>
  <div class="return-address">2290 Larkspur Lane #204<br>Alder Creek, CA 90817</div>
  <div class="gold-rule"></div>
</section>

<section class="sheet label">
  <div class="brand"><span class="brand-mark"></span><div class="brand-name">Halvorsen<small>INSURANCE SERVICES</small></div></div>
  <div class="label-address">2290 Larkspur Lane #204<br>Alder Creek, CA 90817</div>
</section>

</body>
</html>
```